KT Automation - Stationery and Identity.

Corporate Identity Design for the company, which includes Power Point presentations, Letterheads, business cards and mail signatures. We look for a simple design, but modern and elegant, that goes hand in hand with the technology that is the engine of the company.

Target Market(s)

Industrial Sector of Automation, Robotics and Process Control.

Industry/Entity Type

Automation

Colors

Designer to choose colors to be used in the design.

Requirements
Must have
• It must have an elegant, simple and clean design.

```html
<!DOCTYPE html>
<html lang="en">
<head>
<meta charset="utf-8">
<title>KT Automation – Business Card</title>
<link rel="stylesheet" href="https://fonts.googleapis.com/css2?family=Open+Sans:wght@400;600;700&display=swap">
<style>
  :root {
    --bg: #2b2b2d;
    --blue: #1e8fd0;
    --blue-light: #2aa6df;
    --blue-dark: #1560a8;
    --ink: #4a4a4f;
    --grey: #8d8d92;
    --white: #ffffff;
    --wash: #eef4f9;
  }
  * { box-sizing: border-box; margin: 0; padding: 0; }
  html, body { width: 1200px; height: 892px; overflow: hidden; }
  body {
    background: var(--bg);
    font-family: "Open Sans", Arial, sans-serif;
    position: relative;
  }
  .card {
    position: absolute;
    width: 540px;
    height: 309px;
    box-shadow: 0 14px 30px rgba(0,0,0,.45);
    overflow: hidden;
  }
  /* Back of the card */
  .card-back {
    left: 60px; top: 80px;
    background: linear-gradient(135deg, var(--blue-light), var(--blue));
    color: var(--white);
  }
  .card-back .brand {
    position: absolute;
    left: 0; right: 0; top: 118px;
    text-align: center;
    font-weight: 700;
    font-size: 30px;
    letter-spacing: 1px;
  }
  .card-back .web {
    position: absolute;
    left: 0; right: 0; bottom: 34px;
    text-align: center;
    font-size: 13px;
  }
  /* Front of the card */
  .card-front {
    left: 600px; top: 500px;
    background: var(--white);
    color: var(--ink);
  }
  .card-front .wash {
    position: absolute;
    left: 0; top: 110px;
    width: 300px; height: 199px;
    background: linear-gradient(90deg, var(--wash), rgba(238,244,249,0));
  }
  .card-front .brand {
    position: absolute;
    right: 30px; top: 38px;
    display: flex; align-items: center; gap: 10px;
    font-weight: 600;
    font-size: 22px;
    letter-spacing: 2px;
    color: var(--grey);
  }
  .card-front .brand-square {
    width: 16px; height: 16px;
    background: var(--blue);
  }
  .holder {
    position: absolute;
    left: 38px; top: 150px;
  }
  .holder-accent {
    position: absolute;
    left: 0; top: 152px;
    width: 16px; height: 30px;
    background: var(--blue);
  }
  .holder .name {
    font-weight: 700;
    font-size: 20px;
    color: var(--blue-dark);
    text-transform: uppercase;
    line-height: 1.1;
  }
  .holder .role {
    font-size: 13px;
    color: var(--grey);
    text-transform: uppercase;
    letter-spacing: .5px;
  }
  .contact {
    position: absolute;
    right: 30px; top: 92px;
    text-align: right;
    font-size: 12.5px;
    line-height: 19px;
    color: var(--ink);
  }
  .contact li { list-style: none; display: flex; justify-content: flex-end; align-items: center; gap: 6px; }
  .contact svg { width: 12px; height: 12px; fill: var(--blue-dark); }
  .email {
    position: absolute;
    left: 210px; bottom: 52px;
    font-size: 13px;
    color: var(--ink);
  }
  .web-band {
    position: absolute;
    right: 0; bottom: 0;
    width: 270px; height: 40px;
    background: var(--blue);
    color: var(--white);
    font-size: 14px;
    display: flex; align-items: center; justify-content: center;
  }
</style>
</head>
<body>

  <section class="card card-back">
    <div class="brand">KT Automation</div>
    <div class="web">www.ktautomation.mx</div>
  </section>

  <section class="card card-front">
    <div class="wash"></div>

    <div class="brand"><span class="brand-square"></span>KT Automation</div>

    <ul class="contact">
      <li>Av. Los Robles No. 210</li>
      <li>Col. Jardines del Valle C.P. 45100</li>
      <li>Zapopan, Jalisco, Mexico</li>
      <li>(+52) 33-4100-2255
        <svg viewBox="0 0 24 24"><path d="M6.6 10.8a15.1 15.1 0 0 0 6.6 6.6l2.2-2.2a1 1 0 0 1 1-.25 11.4 11.4 0 0 0 3.6.57 1 1 0 0 1 1 1V20a1 1 0 0 1-1 1A17 17 0 0 1 3 4a1 1 0 0 1 1-1h3.5a1 1 0 0 1 1 1c0 1.25.2 2.45.57 3.57a1 1 0 0 1-.25 1z"/></svg>
      </li>
      <li>33-5500-7788
        <svg viewBox="0 0 24 24"><path d="M7 1h10a2 2 0 0 1 2 2v18a2 2 0 0 1-2 2H7a2 2 0 0 1-2-2V3a2 2 0 0 1 2-2zm0 3v15h10V4z"/></svg>
      </li>
      <li>dortiz@ktautomation.mx
        <svg viewBox="0 0 24 24"><path d="M2 5h20v14H2zm2 2v.5l8 5 8-5V7z"/></svg>
      </li>
    </ul>

    <span class="holder-accent"></span>
    <div class="holder">
      <div class="name">Daniel Ortiz</div>
      <div class="role">President</div>
    </div>

    <div class="email">dortiz@ktautomation.mx</div>
    <div class="web-band">www.ktautomation.mx</div>
  </section>

</body>
</html>
```